German Auto Restoration Website Design

We are working with a Classic Car Restoration company in California.
They compete with guys like this:
https://brackenmotorworks.com

We could not find any auto restoration company websites for inspiration. We attached some images of the type of work they do.

Thank you for taking the time to consider designing a website for us. We are web developers based in Stockton, CA, USA. Most of our projects go through the same process. Understanding this process may help you win a project with us. We custom-code all of our websites in-house. We don’t have any requirements as to what tools you use for your design, but we ask that you follow these guidelines.

IMAGES:
If you use any images or icons in the design, we ask that you have a link to the asset so we can purchase the image/icon. Most of the designs we submit do not have the customer’s images on them unless they have some great images. Be creative; show us the feeling you are trying to portray with your image choices. Use any royalty-free site you choose. We subscribe to Quillon and mainly use their images, but we can purchase images outside of Quillon. PLEASE NOTE: we will not submit designs to clients with watermarks on the images.

FONTS:
We ask that you identify the fonts you’re using in the design. This can be done in a message if you want. We typically use Vantrel Fonts and Quillon Fonts.

CONTENT:
We're always open to different content and ideas. We often submit designs with stock images so the client can see our vision. We typically take pictures after the website launch to use their images with our vision. Lorem Ipsum is fine for paragraphs, but we ask that you make the Headers with correct English. We want to be able to show the vision and identify the sections of the website.

INSPIRATION:
We typically add a couple of links in the brief of websites we like to help you get started in your design.

REVISIONS:
We do not often ask for revisions of the designs unless we see something in the design that may not appeal to the client. If there are slight changes that we want to make, we do that in the development process.

FEEDBACK:
We rarely give feedback on designs during the design process. We are working on many website projects and do not have the time to provide feedback. We usually respond if your request is well thought out and asks specific questions, but a note asking “feedback, please” usually goes unanswered.

```html
<!DOCTYPE html>
<html lang="en">
<head>
<meta charset="utf-8">
<title>Hallberg Restorations — Classic Car Restoration</title>
<link href="https://fonts.googleapis.com/css2?family=Catamaran:wght@300;400;500;600;700;800&display=swap" rel="stylesheet">
<style>
:root{
  --black:#0b0b0b;
  --dark:#1f1f1f;
  --panel:#262626;
  --card:#2f2f2f;
  --card-2:#2c2c2c;
  --maroon:#140505;
  --yellow:#f7d51d;
  --red:#e31e24;
  --white:#ffffff;
  --muted:#bdbdbd;
  --nav-grey:#8c8c8c;
  --line:#d9d9d9;
}
*{box-sizing:border-box;margin:0;padding:0}
html,body{width:1200px;height:3859px;overflow:hidden;background:var(--dark)}
body{font-family:"Catamaran",sans-serif;color:var(--white);position:relative}
.wrap{width:756px;margin:0 auto;position:relative}
.accent{color:var(--yellow)}
section,header,footer{position:relative;overflow:hidden}

/* top bar */
.topbar{height:37px;background:var(--black);font-size:12px}
.topbar .wrap{display:flex;justify-content:space-between;align-items:center;height:37px}
.topbar span{display:flex;align-items:center;gap:12px}
.topbar svg{width:15px;height:15px}

/* nav */
.nav{height:63px;background:linear-gradient(90deg,#8e8e8e,#a3a3a3 55%,#b8b0a0)}
.nav .wrap{display:flex;justify-content:space-between;align-items:center;height:63px}
.brand{display:flex;align-items:center;gap:8px;font-weight:700;font-size:13px;letter-spacing:1.5px;color:var(--black);text-transform:uppercase}
.brand i{width:12px;height:12px;background:var(--black);display:block}
.menu{display:flex;gap:26px;font-size:12.5px;font-weight:600}
.menu a{color:var(--white);text-decoration:none}
.menu a.active{color:var(--yellow)}

/* hero */
.hero{height:475px;background:var(--panel)}
.hero-photo{position:absolute;left:598px;top:0;width:602px;height:475px;background:linear-gradient(160deg,#c59a57 0%,#6b6a5f 30%,#2c3a4f 60%,#5a5a58 100%)}
.hero-text{position:absolute;left:226px;top:152px}
.hero h1{font-size:28px;font-weight:700;line-height:34px}
.hero p{font-size:12.5px;line-height:19px;margin-top:16px;width:220px}
.btn{display:inline-block;background:var(--red);color:var(--white);font-size:12px;font-weight:700;border-radius:2px;text-align:center}
.hero .btn{margin-top:16px;width:132px;height:34px;line-height:34px}

/* stats */
.stats{height:132px;background:var(--maroon)}
.stats .wrap{display:flex;height:132px;align-items:center}
.stat{width:214px}
.stat b{display:block;font-size:38px;font-weight:300;line-height:40px}
.stat small{font-size:13px;color:var(--muted)}

/* about */
.about{height:491px;background:#1c1c1c}
.about-photo{position:absolute;left:0;top:0;width:597px;height:491px;background:radial-gradient(ellipse at 40% 55%,#5a4a4a 0%,#2a2222 40%,#101010 80%)}
.play{position:absolute;left:296px;top:217px;width:62px;height:62px;border-radius:50%;background:var(--red)}
.play svg{position:absolute;left:22px;top:19px}
.about-text{position:absolute;left:614px;top:96px;width:370px}
.about h2{font-size:28px;font-weight:700;margin-bottom:14px}
.about p{font-size:12px;line-height:19.5px;margin-bottom:19px}

/* services */
.services{height:615px;background:var(--panel);text-align:center}
.section-title{font-size:28px;font-weight:700;line-height:34px}
.section-sub{font-size:12.5px;margin-top:8px}
.services .section-title{padding-top:64px}
.cards{display:flex;gap:13px;margin-top:34px;text-align:left}
.svc{width:179px;height:328px;background:var(--card)}
.svc .pic{height:118px}
.svc .body{padding:18px 15px}
.svc h3{font-size:13.5px;font-weight:700;line-height:18px;height:48px}
.svc p{font-size:11.5px;line-height:19.5px;color:#e6e6e6}
.svc a{display:block;margin-top:6px;color:var(--yellow);font-weight:700;font-size:12px;text-decoration:none}
.carousel{display:flex;justify-content:center;align-items:center;gap:14px;margin-top:34px}
.arrow{width:32px;height:32px;border-radius:50%;background:var(--red);display:flex;align-items:center;justify-content:center}
.dot{width:7px;height:7px;border-radius:50%;background:var(--white)}
.dot.on{background:var(--red);margin-left:-8px}

/* advantage */
.advantage{height:489px;background:linear-gradient(90deg,#2a3440 0%,#1a2029 40%,#0d1116 70%,#0a0c0f 100%);text-align:center}
.advantage .section-title{padding-top:66px}
.adv-cards{display:flex;gap:13px;margin-top:34px;text-align:left}
.adv{width:179px;height:256px;border:1.5px solid var(--line);padding:22px 14px}
.adv svg{width:30px;height:30px}
.adv h3{font-size:12.5px;font-weight:700;line-height:17px;margin:20px 0 14px}
.adv p{font-size:11.5px;line-height:17.5px;color:#e6e6e6}

/* gallery */
.gallery{height:652px;background:var(--panel);text-align:center}
.gallery .section-title{padding-top:70px}
.grid{display:grid;grid-template-columns:repeat(3,243px);grid-auto-rows:132px;gap:13px;margin-top:36px}
.tile{position:relative}
.tile.hover{background:#d9423b}
.tile.hover span{position:absolute;left:0;right:0;top:50px;font-size:10px}
.tile.hover svg{position:absolute;left:106px;top:20px}

/* contact */
.contact{height:583px;background:#1e1e1e}
.contact-side{position:absolute;left:610px;top:0;width:590px;height:583px;background:#2d2d2d}
.form{position:absolute;left:226px;top:76px;width:308px}
.contact h2{font-size:28px;font-weight:700}
.contact .lead{font-size:12px;margin-top:6px}
.form label{display:block;font-size:12px;font-weight:700;margin:30px 0 8px}
.form label+.field{margin-top:0}
.form label.next{margin-top:17px}
.field{height:38px;background:#333;font-size:9px;color:#888;padding:14px 13px}
.field.area{height:126px}
.form .btn{width:98px;height:33px;line-height:33px;margin-top:32px}
.info{position:absolute;left:673px;top:76px}
.info p{font-size:12px;margin-top:26px}
.info p.lead{margin-top:6px}
.info h2.again{margin-top:70px}
.socials{display:flex;gap:6px;margin-top:20px}
.socials i{width:14px;height:14px;border-radius:50%;background:var(--white);display:block}

/* footer */
.footer{height:322px;background:#222}
.footer-wedge{position:absolute;left:0;top:0}
.foot-brand{position:absolute;left:232px;top:68px}
.foot-brand .brand{color:var(--black);font-size:11px}
.foot-brand .socials{margin-top:14px;margin-left:30px}
.foot-col{position:absolute;top:60px;font-size:12px;font-weight:600}
.foot-col h4{color:var(--yellow);font-size:12px;font-weight:700;letter-spacing:.5px;margin-bottom:22px}
.foot-col li{list-style:none;margin-bottom:18px}
.foot-col.legal li{margin-bottom:27px}
.news-field{width:180px;height:34px;background:#333;font-size:9px;color:#888;padding:12px 12px;font-weight:400}
.footer .btn{width:180px;height:32px;line-height:32px;margin-top:10px}
.bottom{position:absolute;left:226px;top:298px;width:756px;display:flex;justify-content:space-between;font-size:7.5px;font-weight:600}
</style>
</head>
<body>

<header class="topbar">
  <div class="wrap">
    <span><svg viewBox="0 0 16 16"><circle cx="8" cy="8" r="8" fill="#fff"/><path d="M8 3.5a3 3 0 0 0-3 3c0 2.3 3 5.5 3 5.5s3-3.2 3-5.5a3 3 0 0 0-3-3z" fill="#0b0b0b"/><circle cx="8" cy="6.5" r="1.1" fill="#fff"/></svg>2417 Cedar Mill Road, Fresno CA 93711</span>
    <span><svg viewBox="0 0 16 16"><circle cx="8" cy="8" r="8" fill="#fff"/><rect x="4" y="5" width="8" height="6" rx="1" fill="none" stroke="#0b0b0b" stroke-width="1.2"/><path d="M4 5.5l4 3 4-3" fill="none" stroke="#0b0b0b" stroke-width="1.2"/></svg>hello@hallbergrestore.com</span>
    <span><svg viewBox="0 0 16 16"><circle cx="8" cy="8" r="8" fill="#fff"/><path d="M5.5 4l1.5 0 .7 2-1 .8a5 5 0 0 0 2 2l.8-1 2 .7v1.5c0 .5-.5 1-1 1A6.5 6.5 0 0 1 4.5 5c0-.5.5-1 1-1z" fill="#0b0b0b"/></svg>555-014-2280</span>
  </div>
</header>

<nav class="nav">
  <div class="wrap">
    <div class="brand"><i></i>Hallberg Restorations</div>
    <div class="menu">
      <a class="active">Home</a><a>About Us</a><a>Restoration Services</a><a>Portfolio</a><a>Contact Us</a>
    </div>
  </div>
</nav>

<section class="hero">
  <div class="hero-text">
    <h1>Restoring the Classics,<br><span class="accent">Reviving the Passion</span></h1>
    <p>Expertise and Dedication in Restoring Automotive Heritage</p>
    <a class="btn">Contact Us</a>
  </div>
  <div class="hero-photo" role="img" aria-label="Photo of a restored dark blue classic coupe parked outside a glass building at sunset"></div>
</section>

<section class="stats">
  <div class="wrap">
    <div class="stat"><b>20+</b><small>Years of Experience</small></div>
    <div class="stat"><b>15k+</b><small>Vehicles Restored</small></div>
    <div class="stat" style="width:232px"><b>13</b><small>Technicians &amp; Advisors</small></div>
    <div class="stat"><b>100%</b><small>Client Satisfaction</small></div>
  </div>
</section>

<section class="about">
  <div class="about-photo" role="img" aria-label="Photo of a striped racing classic car from behind in a dark garage">
    <div class="play"><svg width="20" height="24" viewBox="0 0 20 24"><path d="M2 1l17 11L2 23z" fill="#fff"/></svg></div>
  </div>
  <div class="about-text">
    <h2>About <span class="accent">Us</span></h2>
    <p>Hallberg Restorations, your ultimate destination for preserving and reviving classic automobiles. We are a passionate team of dedicated professionals with a deep appreciation for the timeless beauty and engineering excellence found in vintage cars.</p>
    <p>At Hallberg Restorations, we specialize in the meticulous restoration of classic cars, ensuring that each vehicle we work on receives the utmost care and attention to detail.</p>
    <p>Our mission is to breathe new life into these automotive legends, allowing enthusiasts and collectors to relish in their glory once again.</p>
  </div>
</section>

<section class="services">
  <div class="wrap">
    <h2 class="section-title">Our Restoration <span class="accent">Services</span></h2>
    <p class="section-sub">Unleashing the Potential of Vintage Gems</p>
    <div class="cards">
      <article class="svc"><div class="pic" role="img" aria-label="Photo of a workshop with classic cars under restoration" style="background:linear-gradient(180deg,#9a9a9a,#4d4d4d)"></div>
        <div class="body"><h3>Partial Restorations</h3><p>Expert craftsmanship and attention to detail breathe new life into your classic car, enhancing its aesthetic and performance.</p><a>Read More »</a></div></article>
      <article class="svc"><div class="pic" role="img" aria-label="Photo of a damaged car front after an accident" style="background:linear-gradient(180deg,#7a7f86,#2e3136)"></div>
        <div class="body"><h3>Accident Restoration</h3><p>Meticulous repairs restore your classic car after an accident, bringing back its original beauty and integrity.</p><a>Read More »</a></div></article>
      <article class="svc"><div class="pic" role="img" aria-label="Photo of a painter spraying a car body in a paint booth" style="background:linear-gradient(180deg,#c9d3da,#8e9aa3)"></div>
        <div class="body"><h3>Partial Painting &amp; Finishing</h3><p>Elevate your cherished vehicle's appeal with flawless painting and finishing services using premium materials.</p><a>Read More »</a></div></article>
      <article class="svc"><div class="pic" role="img" aria-label="Photo of a blue classic coupe front in warm light" style="background:linear-gradient(180deg,#c9a24a,#34506e)"></div>
        <div class="body"><h3>Mechanical Upgrades</h3><p>Unleash your classic car's potential with engine enhancements and suspension improvements, preserving.</p><a>Read More »</a></div></article>
    </div>
    <div class="carousel">
      <span class="arrow"><svg width="14" height="14" viewBox="0 0 14 14"><path d="M13 7H2M6 2.5L1.5 7 6 11.5" stroke="#fff" stroke-width="1.8" fill="none"/></svg></span>
      <span class="dot"></span><span class="dot on"></span>
      <span class="arrow"><svg width="14" height="14" viewBox="0 0 14 14"><path d="M1 7h11M8 2.5L12.5 7 8 11.5" stroke="#fff" stroke-width="1.8" fill="none"/></svg></span>
    </div>
  </div>
</section>

<section class="advantage" role="img" aria-label="Background photo of a dim workshop hall with mechanics walking">
  <div class="wrap">
    <h2 class="section-title">The <span class="accent">Hallberg Restorations</span> Advantage</h2>
    <p class="section-sub">Choose Quality and Expertise to Keep Your Vehicle in Top Condition</p>
    <div class="adv-cards">
      <article class="adv"><svg viewBox="0 0 30 30"><rect x="2" y="13" width="6" height="4" fill="#f7d51d"/><rect x="9" y="8" width="12" height="14" rx="1" fill="#f7d51d"/><rect x="22" y="13" width="6" height="4" fill="#f7d51d"/><rect x="13" y="4" width="4" height="3" fill="#f7d51d"/></svg>
        <h3>Genuine OEM<br>Parts Warranty</h3><p>Designed and manufactured by the original vehicle manufacturer, provide optimal performance, and covered under the original factory warranty.</p></article>
      <article class="adv"><svg viewBox="0 0 30 30"><path d="M15 2l11 4v8c0 7-5 12-11 14C9 26 4 21 4 14V6z" fill="#f7d51d"/><circle cx="15" cy="15" r="6" fill="none" stroke="#111" stroke-width="1.6"/><path d="M12 15l2.2 2.2L18.5 13" stroke="#111" stroke-width="1.6" fill="none"/></svg>
        <h3>Satisfaction<br>Guaranteed</h3><p>At Hallberg Restorations, we understand that our clients are the foundation of our success. That's why we prioritize customer satisfaction above all else</p></article>
      <article class="adv"><svg viewBox="0 0 30 30"><path d="M4 14L16 3h10v10L15 25z" fill="#f7d51d"/><circle cx="21" cy="8" r="2" fill="#111"/><text x="11" y="19" font-size="8" font-weight="700" fill="#111" font-family="Catamaran,sans-serif">$</text></svg>
        <h3>Fair And<br>Transparent Pricing</h3><p>At Hallberg Restorations, we offer fair and transparent pricing with honest and accurate estimates for all services. No surprises, no unexpected fees or charges.</p></article>
      <article class="adv"><svg viewBox="0 0 30 30"><circle cx="15" cy="14" r="10" fill="#f7d51d"/><rect x="3" y="12" width="4" height="7" rx="1" fill="#f7d51d"/><rect x="23" y="12" width="4" height="7" rx="1" fill="#f7d51d"/><circle cx="11" cy="14" r="1.4" fill="#111"/><circle cx="15" cy="14" r="1.4" fill="#111"/><circle cx="19" cy="14" r="1.4" fill="#111"/><path d="M15 24h5" stroke="#f7d51d" stroke-width="2"/></svg>
        <h3>Best<br>Customer Support</h3><p>Getting your everyday questions answered is both simple and convenient. As soon as you send your inquiry in, we'll respond as soon as possible.</p></article>
    </div>
  </div>
</section>

<section class="gallery">
  <div class="wrap">
    <h2 class="section-title">Reviving the <span class="accent">Past</span></h2>
    <p class="section-sub">Inspiring Images of our Classic Car Restorations</p>
    <div class="grid">
      <div class="tile hover" role="img" aria-label="Photo of a red classic coupe with zoom overlay"><svg width="30" height="30" viewBox="0 0 30 30"><circle cx="12" cy="12" r="9" fill="none" stroke="#fff" stroke-width="2"/><path d="M19 19l8 8M12 8v8M8 12h8" stroke="#fff" stroke-width="2"/></svg><span>Zoom In</span></div>
      <div class="tile" role="img" aria-label="Photo of silver and blue classic cars under a cloudy sky" style="background:linear-gradient(180deg,#9fb0c0,#6b7684)"></div>
      <div class="tile" role="img" aria-label="Photo of a blue classic coupe outside a glass building" style="background:linear-gradient(150deg,#c4a35b,#3b4a5c)"></div>
      <div class="tile" role="img" aria-label="Photo of a white vintage car by green hills" style="background:linear-gradient(180deg,#5d8a4a,#bfc1b9)"></div>
      <div class="tile" role="img" aria-label="Close-up photo of a blue classic car headlight" style="background:linear-gradient(150deg,#e7b33e,#254a74)"></div>
      <div class="tile" role="img" aria-label="Close-up photo of a black wheel with red brake caliper" style="background:radial-gradient(circle,#555,#111)"></div>
      <div class="tile" role="img" aria-label="Photo of a dark leather car interior with a key" style="background:linear-gradient(150deg,#2c3a36,#0e1412)"></div>
      <div class="tile" role="img" aria-label="Photo of a mechanic working under a lifted car" style="background:linear-gradient(180deg,#d0d0d0,#7a7a7a)"></div>
      <div class="tile" role="img" aria-label="Photo of a racing classic car in a dark garage" style="background:radial-gradient(ellipse at 65% 60%,#4a3a3a,#0e0e0e)"></div>
    </div>
  </div>
</section>

<section class="contact">
  <div class="contact-side"></div>
  <div class="form">
    <h2>Get In <span class="accent">touch</span></h2>
    <p class="lead">Send us a Message, Ask a question.</p>
    <label>Full Name</label><div class="field">Johan..</div>
    <label class="next">Email address</label><div class="field">john2@mail...</div>
    <label class="next">Message</label><div class="field area">Type in your message...</div>
    <a class="btn">Send</a>
  </div>
  <div class="info">
    <h2>Contact <span class="accent">Us</span></h2>
    <p class="lead">Reach out us. We are here to hlep.</p>
    <p><b>Phone No.</b> <span class="accent">555-014-2291</span></p>
    <p><b>Email Address.</b> <span class="accent">hello@hallbergrestore.com</span></p>
    <h2 class="again">Contact <span class="accent">Us</span></h2>
    <div class="socials"><i></i><i></i><i></i></div>
  </div>
</section>

<footer class="footer">
  <svg class="footer-wedge" width="452" height="322" viewBox="0 0 452 322"><path d="M0 0H451L0 322z" fill="#7b7b7b"/></svg>
  <div class="foot-brand">
    <div class="brand"><i></i>Hallberg Restorations</div>
    <div class="socials"><i></i><i></i><i></i></div>
  </div>
  <div class="foot-col" style="left:425px">
    <h4>NAVIGATIONS</h4>
    <ul><li>Home</li><li>About Us</li><li>Portfolio</li><li>Contact Us</li><li>Restoration Services</li></ul>
  </div>
  <div class="foot-col legal" style="left:609px">
    <h4>LEGAL</h4>
    <ul><li>Terms of Use</li><li>Terms &amp; Conditions</li><li>Privacy Policy</li><li>Cookie Policy</li></ul>
  </div>
  <div class="foot-col" style="left:802px">
    <h4>NEWSLETTER</h4>
    <div class="news-field">Enter Your Email..</div>
    <a class="btn">Submit</a>
  </div>
  <div class="bottom"><span>All Rights Reserved</span><span>© 2023, Hallberg Restorations</span><span>Terms Conditions | Privacy &amp; Policy</span></div>
</footer>

</body>
</html>
```